We need a wordpress design that will incorporate a professional color scheme with company logo in a clean layout. The design needs to consider that this will be developed on a responsive theme. Colors are up to the disgner - perhaps blue and gold and black. Client wants a 'modern' look.

Industry/Entity Type

It Company

Font styles to use
Serif
Sans Serif

Requirements
Must have
• Navigation: 1) Home 2) Upcoming Auctions 3) Auction Results 4) Real Estate Listings 5) About Us 6) Our Staff 7) Contact Us
• Colors - a corporate look with professional color scheme. Client thinks current rkmarsh.com is too drab.
• In header - logo (attached) , tagliine (“List your property with us – We sell the world since 1917”) Slideshow, and contact info (64 WREN AVENUE • ROME, GA 30482 • 1-800-555-0148 • info@rkmarsh.com)
• Widgets in sidebar or where appropriate - 1) Email Signup 2) Message of the Day 3) Upcoming Auctions 4) News&Events blog 5) Testimonials 6) Social media - FB, twitter, youtube, pinterest, google+
• Footer will have company logo, association logos (attached) and contact info
Nice to have
• use of drop down menu styling - FAQs / News / Testimonials under the About us menu item

```html
<!DOCTYPE html>
<html lang="en">
<head>
<meta charset="utf-8">
<title>R K Marsh Auction Co.</title>
<link href="https://fonts.googleapis.com/css2?family=Open+Sans:wght@400;600;700&family=Merriweather:wght@400;700&display=swap" rel="stylesheet">
<style>
:root{
  --bark:#3a3020;
  --bark-deep:#2b2417;
  --gold:#b8892c;
  --gold-soft:#c9a24e;
  --ink:#2c2c2c;
  --muted:#6e6a62;
  --paper:#f4f2ee;
  --card:#ffffff;
  --line:#dedad2;
  --panel:#f0ede6;
}
*{box-sizing:border-box;margin:0;padding:0}
html,body{width:1200px;height:2408px;overflow:hidden}
body{background:var(--paper);font-family:"Open Sans",Arial,sans-serif;color:var(--ink);font-size:14px}
.wrap{width:1000px;margin:0 auto;position:relative}

/* header */
.site-header{background:var(--bark);height:140px;color:#fff}
.site-header .wrap{display:flex;align-items:center;height:140px}
.brand{display:flex;align-items:center;gap:12px}
.brand-mark{width:22px;height:22px;background:var(--gold)}
.brand-name{font-family:"Merriweather",Georgia,serif;font-size:30px;font-weight:700;color:#fff;line-height:1}
.brand-sub{font-family:"Merriweather",Georgia,serif;font-size:11px;letter-spacing:3px;color:#fff;margin-top:6px}
.tagline{margin-left:34px;padding-left:24px;border-left:1px solid rgba(255,255,255,.3)}
.tagline small{display:block;font-family:"Merriweather",Georgia,serif;font-style:italic;font-size:13px;color:#e8dcc0}
.tagline strong{display:block;font-size:17px;letter-spacing:2px;margin-top:4px}
.contact{margin-left:auto;font-size:12px;line-height:28px;letter-spacing:.5px}
.contact div{display:flex;align-items:center;gap:10px}
.contact svg{width:13px;height:13px;fill:var(--gold-soft)}

/* nav */
.main-nav{background:var(--bark-deep);height:60px}
.main-nav ul{list-style:none;display:flex;height:60px;align-items:center;width:1000px;margin:0 auto}
.main-nav li{font-size:12px;font-weight:600;color:#fff;padding:0 18px;letter-spacing:.5px}
.main-nav li:first-child{padding-left:0}
.main-nav li+li{border-left:1px solid rgba(255,255,255,.15)}

/* slider */
.hero{position:relative;width:1000px;height:500px;margin:0 auto;background:linear-gradient(180deg,#b9c8d8 0%,#a8b59a 45%,#5e6e3e 75%,#3f4a2a 100%)}
.hero-caption{position:absolute;left:0;bottom:36px;background:rgba(40,33,22,.85);padding:14px 26px;color:#fff}
.hero-caption h3{font-size:15px;font-weight:600;letter-spacing:1px}
.hero-caption p{font-size:12px;color:#d8cfbc;margin-top:4px;letter-spacing:1px}
.dots{position:absolute;right:24px;bottom:40px;display:flex;gap:8px}
.dots span{width:12px;height:12px;border-radius:50%;border:2px solid #fff}
.dots span.on{background:#fff}

/* content */
.content{display:flex;gap:30px;margin-top:46px}
.primary{width:660px}
.sidebar{width:310px}
.section-title{font-size:20px;font-weight:600;color:var(--gold);padding-bottom:12px;border-bottom:1px solid var(--line);margin-bottom:20px}

.listing{display:flex;gap:22px;background:var(--card);padding:20px;margin-bottom:18px;border:1px solid var(--line);height:236px}
.listing-photo{width:160px;height:130px;flex:none;background:linear-gradient(160deg,#8aa06a,#4f6332)}
.listing h4{font-size:15px;font-weight:700;color:var(--gold)}
.listing .status{font-size:12px;color:var(--muted);margin-top:4px}
.meta{font-size:12px;color:var(--muted);display:flex;align-items:center;gap:8px;padding:10px 0;margin:10px 0;border-top:1px solid var(--line);border-bottom:1px solid var(--line)}
.meta svg{width:12px;height:12px;fill:var(--muted)}
.listing .summary{font-size:13px;font-weight:600;line-height:1.5}
.actions{display:flex;gap:6px;margin-top:14px}
.btn{font-size:11px;font-weight:700;color:#fff;padding:8px 14px;letter-spacing:.5px}
.btn-gold{background:var(--gold)}
.btn-dark{background:var(--bark-deep)}

.widget{background:var(--card);border:1px solid var(--line);margin-bottom:20px}
.widget-title{font-size:16px;font-weight:600;color:var(--gold);padding:16px 20px;border-bottom:1px solid var(--line)}
.widget-body{padding:18px 20px;font-size:12px;line-height:1.6;color:var(--muted)}
.signup{display:flex;margin-top:16px}
.signup .field{flex:1;border:1px solid var(--line);padding:10px;font-size:11px;color:#a19d95}
.signup .btn{padding:11px 18px}
.motd{background:var(--panel)}
.motd .widget-title{text-align:center}
.motd .widget-body{text-align:center;font-size:11px;line-height:1.7;color:var(--ink);letter-spacing:.4px}
.motd p+p{margin-top:18px}
.testi .widget-title{display:flex;justify-content:space-between}
.arrows{display:flex;gap:6px}
.arrows span{width:20px;height:20px;border-radius:50%;background:#e6e2d9;display:flex;align-items:center;justify-content:center}
.arrows svg{width:8px;height:8px;stroke:var(--ink);fill:none;stroke-width:2}
.quote{display:flex;gap:10px}
.quote-mark{font-family:"Merriweather",serif;font-size:32px;color:var(--gold);line-height:1}
.author{margin-top:12px;color:var(--ink);font-weight:700}
.author small{display:block;font-weight:400;color:var(--muted)}

/* news */
.news{margin-top:6px}
.news-head{display:flex;justify-content:space-between;align-items:center}
.news-grid{display:flex;gap:22px}
.news-card{width:318px}
.news-photo{height:150px}
.news-card h5{font-size:13px;font-weight:700;margin-top:12px}
.news-card p{font-size:11px;color:var(--muted);line-height:1.6;margin-top:6px}
.read{font-size:11px;font-weight:700;color:var(--ink);margin-top:8px;display:block}

/* footer */
.site-footer{margin-top:96px;border-top:1px solid var(--line)}
.footer-top{display:flex;justify-content:space-between;align-items:center;height:130px}
.footer-brand{display:flex;align-items:center;gap:10px}
.footer-brand .brand-mark{width:18px;height:18px}
.footer-brand span{font-family:"Merriweather",serif;font-size:22px;font-weight:700;color:var(--bark)}
.assoc{display:flex;gap:14px;margin-left:26px}
.assoc span{width:44px;height:44px;border-radius:50%;background:#cfc9bd}
.follow{text-align:right;font-size:11px;font-weight:600;letter-spacing:1px;color:var(--muted)}
.social{display:flex;gap:6px;margin-top:8px;justify-content:flex-end}
.social span{width:26px;height:26px;background:var(--bark-deep)}
.footer-bottom{background:var(--bark-deep);color:#d9d1bf;text-align:center;font-size:11px;line-height:22px;padding:18px 0 30px;letter-spacing:.5px}
</style>
</head>
<body>

<header class="site-header">
  <div class="wrap">
    <div class="brand">
      <span class="brand-mark"></span>
      <div>
        <div class="brand-name">R K Marsh</div>
        <div class="brand-sub">AUCTION CO.</div>
      </div>
    </div>
    <div class="tagline">
      <small>List your property with us</small>
      <strong>WE SELL THE WORLD</strong>
    </div>
    <div class="contact">
      <div><svg viewBox="0 0 12 12"><path d="M6 0a4 4 0 0 0-4 4c0 3 4 8 4 8s4-5 4-8a4 4 0 0 0-4-4zm0 5.5A1.5 1.5 0 1 1 6 2.5a1.5 1.5 0 0 1 0 3z"/></svg>64 WREN AVENUE • ROME, GA 30482</div>
      <div><svg viewBox="0 0 12 12"><path d="M2.5 0l2 2.5-1.2 1.5a7 7 0 0 0 4.7 4.7l1.5-1.2 2.5 2L11 11C5 12 0 7 1 1z"/></svg>1-800-555-0148</div>
      <div><svg viewBox="0 0 12 12"><path d="M0 2h12v8H0zm1 1v.3l5 3.2 5-3.2V3z"/></svg>info@rkmarsh.com</div>
    </div>
  </div>
</header>

<nav class="main-nav">
  <ul>
    <li>HOME</li><li>UPCOMING AUCTIONS</li><li>AUCTION RESULTS</li><li>REAL ESTATE LISTINGS</li><li>ABOUT US</li><li>OUR STAFF</li><li>CONTACT US</li>
  </ul>
</nav>

<section class="hero" role="img" aria-label="Photograph of a two-storey brick house with porch and mature trees">
  <div class="hero-caption">
    <h3>AVAILABLE COMMERCIAL PROPERTY</h3>
    <p>FORT PAYNE, ALABAMA</p>
  </div>
  <div class="dots"><span class="on"></span><span></span><span></span></div>
</section>

<div class="wrap">
  <div class="content">
    <main class="primary">
      <h2 class="section-title">Upcoming Auctions</h2>

      <article class="listing">
        <div class="listing-photo" role="img" aria-label="Photograph of wooded acreage"></div>
        <div>
          <h4>LAFAYETTE, WALKER COUNTY, GA</h4>
          <div class="status">FOR SALE - 5.60 WOODED ACRES</div>
          <div class="meta"><svg viewBox="0 0 12 12"><path d="M6 0a4 4 0 0 0-4 4c0 3 4 8 4 8s4-5 4-8a4 4 0 0 0-4-4z"/></svg>Location: Glass Road | Lafayette, GA 30728</div>
          <div class="summary">5.60 WOODED ACRES | LAFAYETTE, GEORGIA | (Walker County)</div>
          <div class="actions"><span class="btn btn-gold">FOR SALE</span><span class="btn btn-dark">VIEW DETAILS</span></div>
        </div>
      </article>

      <article class="listing">
        <div class="listing-photo" role="img" aria-label="Photograph of open land by a river"></div>
        <div>
          <h4>94 ACRES IN TRION, GA</h4>
          <div class="status">FOR SALE</div>
          <div class="meta"><svg viewBox="0 0 12 12"><path d="M6 0a4 4 0 0 0-4 4c0 3 4 8 4 8s4-5 4-8a4 4 0 0 0-4-4z"/></svg>Hwy. 27 | Trion, GA 30753</div>
          <div class="summary">APPROX. 94 ACRES | IN TRION, GA CHATTOOGA RIVER FRONTAGE</div>
          <div class="actions"><span class="btn btn-gold">FOR SALE</span><span class="btn btn-dark">VIEW DETAILS</span></div>
        </div>
      </article>

      <article class="listing">
        <div class="listing-photo" role="img" aria-label="Photograph of a mobile home on a lot"></div>
        <div>
          <h4>E&amp;K DRIVE OFF VILLANOW MILL CREEK ROAD</h4>
          <div class="status">FOR SALE</div>
          <div class="meta"><svg viewBox="0 0 12 12"><path d="M6 0a4 4 0 0 0-4 4c0 3 4 8 4 8s4-5 4-8a4 4 0 0 0-4-4z"/></svg>Off Villanow Mill Creek Road | Lafayette, GA</div>
          <div class="summary">4.6 ACRES WITH MOBILE HOME LAFAYETTE GA</div>
          <div class="actions"><span class="btn btn-gold">FOR SALE</span><span class="btn btn-dark">VIEW DETAILS</span></div>
        </div>
      </article>

      <article class="listing">
        <div class="listing-photo" role="img" aria-label="Photograph of a commercial building"></div>
        <div>
          <h4>FORT PAYNE, ALABAMA</h4>
          <div class="status">AVAILABLE COMMERCIAL PROPERTY</div>
          <div class="meta"><svg viewBox="0 0 12 12"><path d="M6 0a4 4 0 0 0-4 4c0 3 4 8 4 8s4-5 4-8a4 4 0 0 0-4-4z"/></svg>Hwy. 27 | Trion, GA 30753</div>
          <div class="summary">2615 GAULT AVENUE N. | FORT PAYNE, ALABAMA</div>
          <div class="actions"><span class="btn btn-gold">FOR SALE</span><span class="btn btn-dark">VIEW DETAILS</span></div>
        </div>
      </article>
    </main>

    <aside class="sidebar">
      <section class="widget">
        <h3 class="widget-title">Email Signup</h3>
        <div class="widget-body">
          Subscribe below to receive alerts on Upcoming Auctions. It's free!
          <div class="signup"><span class="field">Enter Your Email Id</span><span class="btn btn-gold">SIGNUP</span></div>
        </div>
      </section>

      <section class="widget motd">
        <h3 class="widget-title">Message of the Day</h3>
        <div class="widget-body">
          <p>IMPROVED AND MOBILE-FRIENDLY WEB SITE COMING SOON!</p>
          <p>CONTACT<br>R K MARSH AUCTION CO.<br>FOR ALL YOUR<br>REAL ESTATE NEEDS</p>
          <p>TURN YOUR ASSETS INTO<br>CASH IN 60 DAYS</p>
          <p>CALL OR EMAIL US FOR MORE<br>INFORMATION</p>
          <p>1-800-555-0148<br>info@rkmarsh.com</p>
        </div>
      </section>

      <section class="widget testi">
        <h3 class="widget-title">Testimonials
          <span class="arrows"><span><svg viewBox="0 0 8 8"><path d="M5 1L2 4l3 3"/></svg></span><span><svg viewBox="0 0 8 8"><path d="M3 1l3 3-3 3"/></svg></span></span>
        </h3>
        <div class="widget-body">
          <div class="quote"><span class="quote-mark">“</span>
            <div>Coosa Valley Savings Bank recently completed an auction of a large parcel of timberland that had been taken back through a foreclosure proceeding. The Bank received a recommendation for and contracted R K Marsh Auction Company to manage it.</div>
          </div>
          <div class="author">Daniel Whitcomb, Jr<small>Coosa Valley Savings Bank</small></div>
        </div>
      </section>
    </aside>
  </div>

  <section class="news">
    <div class="news-head">
      <h2 class="section-title" style="border:0;margin-bottom:14px">News &amp; Events</h2>
      <span class="arrows"><span><svg viewBox="0 0 8 8"><path d="M5 1L2 4l3 3"/></svg></span><span><svg viewBox="0 0 8 8"><path d="M3 1l3 3-3 3"/></svg></span></span>
    </div>
    <div class="news-grid">
      <article class="news-card">
        <div class="news-photo" role="img" aria-label="Photograph of city buildings under a blue sky" style="background:linear-gradient(180deg,#8fb0d2,#6f7b86)"></div>
        <h5>Contrary to popular belief, Lorem Ipsum</h5>
        <p>Many local sales of farmland and homes are planned this spring, with dates posted as soon as each is set.</p>
        <span class="read">READ MORE</span>
      </article>
      <article class="news-card">
        <div class="news-photo" role="img" aria-label="Photograph of a country church in winter" style="background:linear-gradient(180deg,#c9d3dc,#8e8a7c)"></div>
        <h5>The standard chunk of Lorem Ipsum used</h5>
        <p>Our team will be at the county fair this year to meet buyers and answer questions on open lots.</p>
        <span class="read">READ MORE</span>
      </article>
      <article class="news-card">
        <div class="news-photo" role="img" aria-label="Photograph of a lake with wooded shore" style="background:linear-gradient(180deg,#9cb8cf,#4f6a4a)"></div>
        <h5>Sed ut perspiciatis unde omnis iste natus</h5>
        <p>Lakefront tracts draw strong bids as families look for weekend places close to home and water.</p>
        <span class="read">READ MORE</span>
      </article>
    </div>
  </section>
</div>

<footer class="site-footer">
  <div class="wrap footer-top">
    <div style="display:flex;align-items:center">
      <div class="footer-brand"><span class="brand-mark"></span><span>R K Marsh</span></div>
      <div class="assoc"><span></span><span></span></div>
    </div>
    <div class="follow">FOLLOW US ON
      <div class="social"><span></span><span></span><span></span><span></span><span></span></div>
    </div>
  </div>
  <div class="footer-bottom">
    R K MARSH AUCTION CO. • 64 WREN AVENUE • ROME, GA 30482 • PH: 706-555-0171 • 1-800-555-0148 • info@rkmarsh.com<br>
    Copyright © 2009 - 2015 • R K Marsh • All Rights Reserved
  </div>
</footer>

</body>
</html>
```